依頼概要
■ 依頼の目的/概要

小型浄水器の新聞折り込みのプレゼントチラシ

■ デザインへの要望

わかりやすく、シンプルに目立つ感じでおねがいします。小型浄水器の写真は後日アップします。

■ 納品ファイルの希望

高解像度JPG形式/イラストレーター形式/フォトショップ形式のいづれか

■ 利用用途

新聞折り込み等チラシのみ

■ 進め方

弊社の希望するイメージに近い提案を1つ(場合によって複数)選択させて頂きます。希望に近づけるために、修正要望を個別にさせて頂くこともあります。コンペ方式のため、修正後に当選されない場合も、どうかご了承ください。

■ その他/注意点

選択させて頂いたデザインの著作権(財産権)等の扱いはVelmora利用規約に従い、弊社に譲渡をお願いします。フォントや画像素材などを利用する場合は上記利用用途に使用できるこ とを確認し、第三者の知的財産権等に注意して下さい。
応募方法の所を添付資料を参考に作ってほしいと思います。
胚芽米1kg1,800円相当
美味しいお水で美味しいご飯

をプレゼントに足してみてください。
■ 選んだ理由

修正もすぐにして頂いて、有難うございます。

■ 提案者全員へのお礼・コメント

良いデザインでわかりやすかったです。

```html
<!DOCTYPE html>
<html lang="ja">
<head>
<meta charset="utf-8">
<title>AQUANE プレゼントキャンペーン</title>
<link rel="stylesheet" href="https://fonts.googleapis.com/css2?family=Noto+Sans+JP:wght@400;700;900&family=Noto+Serif+JP:wght@500;700&display=swap">
<style>
:root{
  --sky:#d7ecf8;
  --sky-deep:#8fc6ea;
  --blue:#1f7cc8;
  --blue-dark:#0d5a9e;
  --navy:#1b3b63;
  --red:#d6262e;
  --paper:#ffffff;
  --ink:#333;
  --line:#9cc3e2;
}
*{margin:0;padding:0;box-sizing:border-box}
html,body{width:846px;height:1200px;overflow:hidden;background:#fff}
body{font-family:"Noto Sans JP",sans-serif;color:var(--ink)}
.flyer{position:relative;width:846px;height:1200px;background:linear-gradient(#f3f9fd,#e3f1fa);overflow:hidden}
.hero-photo{position:absolute;left:0;top:0;width:846px;height:860px;
  background:radial-gradient(ellipse at 30% 55%,#f4e6dc 0%,#eaf4fb 28%,transparent 50%),
  radial-gradient(ellipse at 80% 20%,#ffffff 0%,transparent 40%),
  linear-gradient(160deg,#bfe0f5 0%,#e8f4fb 45%,#a9d3ef 100%)}
.brand{position:absolute;left:34px;top:36px;display:flex;align-items:center;gap:8px;
  font-weight:700;font-size:26px;color:var(--blue);letter-spacing:2px}
.brand-dot{width:14px;height:14px;border-radius:50%;background:var(--blue)}
.tagline{position:absolute;left:250px;top:90px;writing-mode:vertical-rl;
  font-family:"Noto Serif JP",serif;font-size:21px;line-height:36px;color:var(--navy);letter-spacing:2px}
.tagline em{font-style:normal;color:var(--blue);font-weight:700}
.title{position:absolute;writing-mode:vertical-rl;font-weight:900;color:var(--blue);
  font-size:90px;line-height:1;letter-spacing:4px;text-shadow:0 0 10px #fff}
.title-present{left:700px;top:150px}
.title-campaign{left:585px;top:250px}
.prizes{position:absolute;left:30px;top:640px;width:540px;height:330px;background:var(--paper);
  border:3px solid var(--blue);border-radius:10px}
.prize-tab{position:absolute;left:-3px;top:-3px;background:var(--blue);color:#fff;font-weight:700;
  font-size:19px;padding:6px 18px;border-radius:10px 0 10px 0}
.prize{position:absolute}
.prize-photo{border-radius:6px;background:linear-gradient(#e7edf2,#b9c6d1)}
.prize-name{font-weight:700;font-size:17px;color:var(--navy)}
.prize-note{font-size:11px;color:#666}
.badge{position:absolute;width:78px;height:78px;border-radius:50%;background:var(--red);color:#fff;
  display:flex;flex-direction:column;align-items:center;justify-content:center;font-weight:700;line-height:1.1;font-size:12px}
.badge b{font-size:24px}
.company{position:absolute;left:30px;top:985px;width:550px;height:200px}
.company-row{display:flex;align-items:flex-start;gap:12px;margin-bottom:8px}
.company-label{background:var(--blue);color:#fff;font-size:12px;font-weight:700;padding:3px 10px;border-radius:3px;white-space:nowrap}
.company-text{font-size:13px;line-height:1.5}
.company-text strong{font-size:17px;color:var(--navy)}
.phone{display:flex;align-items:center;gap:12px}
.phone-box{background:var(--blue);color:#fff;font-weight:900;font-size:34px;line-height:1.2;padding:4px 16px;border-radius:6px;letter-spacing:1px;display:flex;align-items:center;gap:8px;white-space:nowrap}
.phone-note{font-size:11px;line-height:1.5;color:#555;white-space:nowrap}
.company-footnote{font-size:11px;line-height:1.5;color:#666}
.postcard{position:absolute;left:600px;top:800px;width:216px;height:370px;background:var(--paper);
  border:1px solid var(--line)}
.postcard-guide{position:absolute;right:14px;top:14px;height:200px;writing-mode:vertical-rl;font-size:11px;line-height:18px;color:#555}
.postcard-title{position:absolute;left:0;right:0;top:232px;text-align:center;font-size:12px;font-weight:700;color:var(--navy);border-top:1px solid var(--line);border-bottom:1px solid var(--line);padding:4px 0}
.postcode{position:absolute;left:40px;top:270px;display:flex;gap:3px}
.postcode span{width:16px;height:22px;border:1px solid var(--red)}
.postcard-lines{position:absolute;left:14px;right:14px;top:306px}
.postcard-lines div{border-bottom:1px dotted var(--line);height:18px}
</style>
</head>
<body>
<main class="flyer">
  <div class="hero-photo" role="img" aria-label="水しぶきの中で目を閉じて水を感じる女性の写真"></div>

  <header class="brand"><span class="brand-dot"></span>AQUANE</header>

  <p class="tagline">なんて、<em>簡単</em>なんだろう。<br>なんて<em>美味しい</em>んだろう。<br>なんて<em>経済的</em>なんだろう。<br>そんな「うれしい」驚き、<br>浄水器にあります。</p>

  <h1 class="title title-present">プレゼント</h1>
  <h1 class="title title-campaign">キャンペーン</h1>

  <section class="prizes">
    <div class="prize-tab">プレゼント内容</div>

    <div class="prize" style="left:24px;top:48px">
      <div class="prize-photo" style="width:220px;height:130px" role="img" aria-label="整水器の製品写真"></div>
    </div>
    <div class="prize" style="left:262px;top:56px">
      <div class="prize-name">Solvane 整水器</div>
      <div class="prize-note">(60,000円相当)</div>
    </div>
    <div class="badge" style="left:400px;top:100px">抽選で<b>1</b>名様限定</div>

    <div class="prize" style="left:24px;top:196px">
      <div class="prize-photo" style="width:100px;height:100px;border-radius:50%" role="img" aria-label="小型浄水器の製品写真"></div>
      <div class="prize-name" style="font-size:14px;margin-top:4px">小型の浄水器</div>
    </div>
    <div class="badge" style="left:140px;top:218px">抽選で<b>100</b>名様</div>

    <div class="prize" style="left:290px;top:188px">
      <div class="prize-name" style="font-size:14px">胚芽米 <span class="prize-note">1kg 1,800円相当</span></div>
      <div class="prize-photo" style="width:110px;height:88px;margin-top:4px;background:linear-gradient(#c98c4f,#8a5a2f)" role="img" aria-label="胚芽米の袋の写真"></div>
      <div class="prize-note" style="margin-top:2px">美味しいお水で美味しいご飯</div>
    </div>
    <div class="badge" style="left:420px;top:218px">抽選で<b>100</b>名様</div>
  </section>

  <section class="company">
    <div class="company-row">
      <span class="company-label">主催</span>
      <p class="company-text"><strong>株式会社 アクアネ</strong> 函館営業所<br>〒041-0000 北海道函館市港町1丁目2番3号</p>
    </div>
    <div class="company-row">
      <span class="company-label">お問合せ</span>
      <div class="phone">
        <span class="phone-box">
          <svg width="26" height="26" viewBox="0 0 24 24" aria-hidden="true"><path fill="#fff" d="M6.6 10.8a15 15 0 0 0 6.6 6.6l2.2-2.2c.3-.3.7-.4 1-.2 1.1.4 2.3.6 3.6.6.6 0 1 .4 1 1V20c0 .6-.4 1-1 1A17 17 0 0 1 3 4c0-.6.4-1 1-1h3.5c.6 0 1 .4 1 1 0 1.3.2 2.5.6 3.6.1.3 0 .7-.2 1z"/></svg>
          0120-48-3710
        </span>
        <p class="phone-note">受付時間 9:00〜18:00<br>土日祝日は休業です</p>
      </div>
    </div>
    <p class="company-footnote">ハガキに必要事項をご記入の上、切り取ってご投函ください。<br>当選者の発表は発送をもってかえさせて頂きます。</p>
  </section>

  <section class="postcard" aria-label="応募はがき">
    <p class="postcard-guide">ご住所・お名前・年齢・<br>電話番号をご記入ください。<br>ご希望の賞品に○をつけて<br>ご応募ください。</p>
    <p class="postcard-title">AQUANEプレゼントキャンペーン</p>
    <div class="postcode"><span></span><span></span><span></span><span></span><span></span><span></span><span></span></div>
    <div class="postcard-lines"><div></div><div></div><div></div></div>
  </section>
</main>
</body>
</html>
```